Business Card Design

Bowen therapy is a gentle therapy where moves are made(using your hands) over muscles or joint areas create myofascial release enabling the body to rebalance itself.

Its relaxing and have heal a variety of aliments . n contrast to other hands-on modalities, where the practitioner imposes correction on the client through manipulation, Bowen Technique facilitates the body in healing itself, with minimal intervention. Because of the subtle nature of Bowen Technique, and the body's continuing response to it over several days thereafter, other forms of manipulative therapy are discouraged for up to five days after a session, as they may interfere with the efficacy of the work.

Its an energy healing work using hands.
Its relaxing but professional.
I'm think of using blues, no greens or yellows. Some wave lines .

Target Market(s)

Anybody-

Industry/Entity Type

Business

Contact Information for Business Card

Marnie's Kessel Therapy,Marnie Fletcher, Bowen Therapist,Cert IV Kinlark
Elmbrook, South Reed Cove, Harlowvale, 0467 305918,Gentle therapy restoring body balance.

Requirements
Must have
• Back needs a appointment table
with this wording :
Bowen Therapy is a subtle gentle bodywork therapy where a series of moves are made over muscles that can be used to address a wide range of conditions. It is suitable for skeletal, joint and muscle problems as well as for babies and children
Date Time.

If you are unable to keep your appointment, please contact us as soon as possible.

0467305918 ozmarnie@fernmail.net
Should not have
• Dont like times new roman and handwritten script font.

```html
<!DOCTYPE html>
<html lang="en">
<head>
<meta charset="utf-8">
<title>Marnie's Kessel Therapy – Business Card</title>
<link rel="stylesheet" href="https://fonts.googleapis.com/css2?family=Roboto+Condensed:wght@300;400&display=swap">
<style>
  :root {
    --page-bg: #d3d3d3;
    --card-bg: #f9f8f8;
    --brand-blue: #4f79bd;
    --text-grey: #5a5a5a;
    --text-dark: #3e3e3e;
    --bloom-light: #efedee;
    --bloom-mid: #d4d1d3;
  }
  * { box-sizing: border-box; margin: 0; padding: 0; }
  html, body {
    width: 1200px;
    height: 1000px;
    overflow: hidden;
    background: var(--page-bg);
    font-family: "Roboto Condensed", "Arial Narrow", sans-serif;
  }
  .business-card {
    position: absolute;
    left: 110px;
    top: 220px;
    width: 980px;
    height: 560px;
    background: radial-gradient(ellipse at 72% 40%, #ffffff 0%, var(--card-bg) 60%, #f2f1f1 100%);
    overflow: hidden;
  }
  .floral-artwork {
    position: absolute;
    left: 500px;
    top: 30px;
    width: 460px;
    height: 500px;
    border-radius: 45% 50% 40% 45%;
    background: radial-gradient(ellipse at 45% 40%, var(--bloom-mid) 0%, var(--bloom-light) 45%, rgba(249,248,248,0) 72%);
  }
  .brand {
    position: absolute;
    left: 88px;
    top: 100px;
    display: flex;
    align-items: center;
    gap: 22px;
  }
  .brand-mark {
    width: 70px;
    height: 70px;
    background: var(--brand-blue);
  }
  .brand-name {
    font-size: 50px;
    font-weight: 300;
    color: var(--brand-blue);
    line-height: 1;
    letter-spacing: -0.5px;
  }
  .brand-tagline {
    font-size: 20px;
    font-weight: 400;
    color: var(--text-grey);
    margin-top: 4px;
    line-height: 1;
  }
  .contact {
    position: absolute;
    left: 118px;
    top: 278px;
  }
  .person-name {
    font-size: 40px;
    font-weight: 300;
    color: var(--brand-blue);
    line-height: 1;
  }
  .person-role {
    font-size: 20px;
    color: var(--text-grey);
    margin-top: 4px;
  }
  .phone {
    font-size: 34px;
    font-weight: 300;
    color: var(--text-dark);
    margin-top: 22px;
    letter-spacing: 0.5px;
  }
  .locations {
    font-size: 21px;
    color: var(--text-grey);
    margin-top: 26px;
    line-height: 1.2;
  }
</style>
</head>
<body>
  <main class="business-card">
    <div class="floral-artwork" role="img" aria-label="Soft grey illustration of two magnolia-like flowers on a branch"></div>

    <header class="brand">
      <div class="brand-mark"></div>
      <div>
        <h1 class="brand-name">Marnie's Kessel Therapy</h1>
        <p class="brand-tagline">Gentle therapy restoring body balance</p>
      </div>
    </header>

    <section class="contact">
      <h2 class="person-name">Marnie Fletcher</h2>
      <p class="person-role">Bowen Therapist / Cert IV Kinlark</p>
      <p class="phone">0467 305918</p>
      <p class="locations">Elmbrook,<br>South Reed Cove, Harlowvale</p>
    </section>
  </main>
</body>
</html>
```